New Look for Existing Website
Keep it simple, clean, crisp & clear
Creative Brief
Automotive
www.bitlocate.ie
We are an advertising website where people search for and view lists of results and associated information for second hand car parts suppliers.
we like Zorvane for its simplicity. We like clean and simple websites, easy to navigate and not cluttered with lots of links/advertisements or too much text.
www.zorvane.ie
http://www.klimbrook.ie/klimbrook/publish/vehicleLookup.jsp
please view the existing website at www.bitlocate.ie and then create new look for the main page/template every are should have its own box/ container with soft borders also logo looks too plain and can be changed if required.

```html
<!DOCTYPE html>
<html lang="en">
<head>
<meta charset="utf-8">
<title>BITLOCATE.IE – Car Dismantlers Search</title>
<link rel="stylesheet" href="https://fonts.googleapis.com/css2?family=Arimo:ital,wght@0,400;0,700;1,700&display=swap">
<style>
:root{
  --white:#ffffff;
  --navy:#1c2f6b;
  --brand-red:#9b1b1b;
  --nav-bg:#e3e9f0;
  --nav-border:#c7d0da;
  --panel-bg:#f3f3f3;
  --panel-border:#d4d4d4;
  --text:#222222;
  --green:#7dc242;
  --button-bg:#e2e2e2;
  --button-border:#bdbdbd;
  --footer-bg:#d6e4ef;
  --chirp:#3d9ad1;
  --friend:#2b4a8c;
  --vid:#c9302c;
}
*{box-sizing:border-box;margin:0;padding:0}
html,body{width:1200px;height:961px;overflow:hidden}
body{position:relative;background:var(--white);font-family:"Arimo",Arial,sans-serif;color:var(--text)}
.header{position:absolute;left:0;top:0;width:1200px;height:143px;background:var(--white)}
.brand{position:absolute;left:104px;top:48px;display:flex;align-items:center;gap:16px}
.brand-dot{width:40px;height:40px;border-radius:50%;background:var(--brand-red)}
.brand-name{font-size:44px;font-weight:700;color:var(--navy);letter-spacing:1px}
.nav{position:absolute;left:0;top:143px;width:1200px;height:51px;background:var(--nav-bg);border-top:1px solid var(--nav-border);border-bottom:1px solid var(--nav-border);display:flex;justify-content:space-around;align-items:center;padding:0 20px}
.nav a{font-size:15px;color:var(--text);text-decoration:none}
.main{position:absolute;left:0;top:194px;width:1200px;height:609px;background:var(--panel-bg);border-bottom:1px solid var(--panel-border)}
.title{position:absolute;top:24px;width:100%;text-align:center;font-size:30px;font-weight:700;color:var(--brand-red)}
.step{position:absolute;top:68px;width:100%;text-align:center;font-size:16px;font-weight:700;font-style:italic;line-height:24px}
.vehicle-box{position:absolute;left:427px;top:187px;width:285px;height:65px;background:var(--white);border:1px solid var(--panel-border);border-radius:4px}
.get-details{position:absolute;left:427px;top:303px;width:311px;height:55px;background:var(--button-bg);border:1px solid var(--button-border);font-size:28px;display:flex;align-items:center;justify-content:center}
.connectors{position:absolute;left:0;top:0}
.field{position:absolute;left:803px;width:117px}
.field label{display:block;font-size:15px;line-height:18px;margin-bottom:2px}
.field span{display:block;height:20px;background:var(--white);border:1px solid var(--panel-border)}
.terms{position:absolute;top:452px;width:100%;text-align:center;font-size:16px;font-weight:700}
.search-btn{position:absolute;left:435px;top:495px;width:285px;height:57px;background:var(--button-bg);border:1px solid var(--button-border);border-radius:3px;font-size:16px;display:flex;align-items:center;justify-content:center}
.footer{position:absolute;left:0;top:803px;width:1200px;height:158px;background:var(--footer-bg)}
.social{position:absolute;top:30px;display:flex;align-items:center;gap:10px;font-size:22px;font-weight:700}
.social i{width:70px;height:70px;border-radius:8px}
.chirp{left:40px;color:var(--chirp)} .chirp i{background:var(--chirp)}
.friend{left:235px;color:var(--friend)} .friend i{background:var(--friend)}
.vid{left:445px;color:var(--vid)} .vid i{background:var(--vid)}
.footer-brand{position:absolute;left:870px;top:26px;width:300px}
.footer-name{font-size:36px;font-weight:700;color:var(--brand-red)}
.footer-note{font-size:14px;line-height:18px;color:var(--text);margin-top:6px}
.footer-note em{color:var(--brand-red);font-style:normal}
</style>
</head>
<body>
<header class="header">
  <div class="brand"><span class="brand-dot"></span><span class="brand-name">BITLOCATE.IE</span></div>
</header>
<nav class="nav">
  <a>Parts Search</a><a>Part Request</a><a>Damaged Repariables</a><a>About</a><a>Contact</a><a>Dismantlers by Map</a><a>Dismantlers by List</a>
</nav>
<main class="main">
  <h1 class="title">Car Dismantlers - Car Parts Search</h1>
  <p class="step">Step 1 of 3 ...<br>.Select the Make, Model &amp; Year of the vehicle for which you require parts!</p>
  <div class="vehicle-box"></div>
  <div class="get-details">GET DETAILS</div>
  <svg class="connectors" width="1200" height="609" viewBox="0 0 1200 609">
    <g stroke="var(--green)" stroke-width="5" fill="var(--green)">
      <line x1="572" y1="252" x2="572" y2="290"/>
      <polygon points="563,286 581,286 572,300" stroke="none"/>
      <line x1="712" y1="220" x2="746" y2="220"/>
      <line x1="738" y1="330" x2="746" y2="330"/>
      <line x1="746" y1="207" x2="746" y2="389"/>
      <line x1="746" y1="207" x2="782" y2="207"/><polygon points="780,199 780,215 794,207" stroke="none"/>
      <line x1="746" y1="259" x2="782" y2="259"/><polygon points="780,251 780,267 794,259" stroke="none"/>
      <line x1="746" y1="293" x2="782" y2="293"/><polygon points="780,285 780,301 794,293" stroke="none"/>
      <line x1="746" y1="342" x2="782" y2="342"/><polygon points="780,334 780,350 794,342" stroke="none"/>
      <line x1="746" y1="389" x2="782" y2="389"/><polygon points="780,381 780,397 794,389" stroke="none"/>
    </g>
  </svg>
  <div class="field" style="top:182px"><label>Car make</label><span></span></div>
  <div class="field" style="top:228px"><label>Car Model</label><span></span></div>
  <div class="field" style="top:278px"><label>Any year</label><span></span></div>
  <div class="field" style="top:330px"><label>Any category</label><span></span></div>
  <div class="field" style="top:376px"><label>Any part</label><span></span></div>
  <p class="terms">By clicking the Search button below you are agreeing with the Terms &amp; Conditions</p>
  <div class="search-btn">SEARCH CAR DISMANTLERS</div>
</main>
<footer class="footer">
  <div class="social chirp"><i></i>Chirply</div>
  <div class="social friend"><i></i>Friendlane</div>
  <div class="social vid"><i></i>Vidstream</div>
  <div class="footer-brand">
    <div class="footer-name">BITLOCATE.IE</div>
    <p class="footer-note">© 2008 - 2011 <em>www.bitlocate.ie</em><br>Car Dismantlers &amp; Car Breakers Search<br>for Ireland</p>
  </div>
</footer>
</body>
</html>
```